Geschäftspapiere
Zielgruppe
Die TIVA Salbe gibt ein zuverlässige Gefühl, durch ein innovatives Naturprodukt erstaunlich schnelle, wirkungsvolle Hilfe bei Schmerzen des Bewegungsapparates und bei Hautschäden zu erhalten und dabei gleichzeitig die Haut zu pflegen.
Wir wollen jetzt stärker auf die Zielgruppe TCM Praxis, Chiropraktiker, Physiotherapie gehen und wollen nun eine Preisliste dafür erstellen.
Aufgabenstellung
Zielgruppe ist B2B, TCM Praxis, Chiropraktiker, Physiotherapie.
Die Preisliste sollte auf den Briefpapier erstellt werden. Bitte an Farben, Logos etc. von der Webseite nehmen.

```html
<!DOCTYPE html>
<html lang="de">
<head>
<meta charset="utf-8">
<title>TIVA Naturbalsame – Preisliste</title>
<link href="https://fonts.googleapis.com/css2?family=Source+Sans+3:wght@400;600;700;800&display=swap" rel="stylesheet">
<style>
  :root{
    --amber:#e3a011;
    --amber-dark:#c98a08;
    --amber-light:#f0bd4a;
    --ink:#1d1d1d;
    --grey:#5f6266;
    --paper:#fbfbfb;
    --backdrop:#e6ebe7;
    --white:#ffffff;
  }
  *{box-sizing:border-box;margin:0;padding:0}
  html,body{width:1200px;height:1012px;overflow:hidden;background:var(--backdrop);
    font-family:"Source Sans 3",sans-serif;color:var(--grey)}
  .sheet{position:absolute;left:263px;top:23px;width:673px;height:965px;background:var(--paper);
    overflow:hidden;box-shadow:0 2px 10px rgba(0,0,0,.12)}
  .edge-rule{position:absolute;right:0;top:0;width:3px;height:100%;background:var(--amber)}

  .logo-disc{position:absolute;left:431px;top:-50px;width:224px;height:224px;border-radius:50%;
    background:var(--white);box-shadow:0 4px 4px -1px rgba(0,0,0,.22)}
  .brand-dot{position:absolute;left:466px;top:58px;width:36px;height:36px;border-radius:50%;background:var(--amber)}
  .brand-name{position:absolute;left:514px;top:40px;font-size:48px;font-weight:800;color:var(--ink);line-height:1;letter-spacing:-1px}
  .brand-sub{position:absolute;left:506px;top:93px;font-size:12px;letter-spacing:2.6px;color:var(--grey)}
  .brand-tag{position:absolute;left:506px;top:115px;font-size:12.5px;font-weight:600;letter-spacing:1.3px;color:var(--amber)}

  .sender{position:absolute;left:78px;top:156px;font-size:7px;color:var(--grey)}
  .sender b{font-weight:700}

  .title{position:absolute;left:78px;top:271px;font-size:14.5px;font-weight:800;color:var(--amber);letter-spacing:.3px}
  .title-rule{position:absolute;left:0;top:289px;width:166px;height:1.5px;background:var(--amber)}
  .fold-mark{position:absolute;left:0;top:339px;width:11px;height:1.5px;background:var(--amber)}
  .intro{position:absolute;left:78px;top:298px;width:560px;font-size:10.5px;line-height:18px;color:var(--grey)}

  .tier{position:absolute;top:422px;width:144px;height:362px}
  .tier-body{position:absolute;inset:0;background:var(--amber);border-radius:8px 8px 70px 70px / 8px 8px 22px 22px;
    box-shadow:0 3px 0 #9a9a9a}
  .tier-body::after{content:"";position:absolute;left:6px;right:6px;top:4px;height:100px;border-radius:6px;
    background:linear-gradient(180deg,rgba(255,255,255,.22),rgba(255,255,255,0))}
  .medal{position:absolute;left:28px;top:-34px;width:88px;height:88px;border-radius:50%;
    background:var(--white);border:4px solid var(--amber-light);box-shadow:0 0 0 2px var(--amber-dark)}
  .medal-art{position:absolute;inset:6px;border-radius:50%;background:radial-gradient(circle,#f7e3b0,#e6c16a)}
  .tier-label{position:absolute;left:7px;right:7px;top:74px;height:23px;background:var(--white);
    text-align:center;font-size:18px;font-weight:800;color:var(--amber);line-height:23px;letter-spacing:.5px}
  .tier-qty,.tier-price{position:absolute;left:0;right:0;text-align:center;color:var(--white);font-weight:600}
  .tier-qty{top:113px;font-size:17px}
  .tier-price{top:160px;font-size:15px}
  .tier-rule{position:absolute;left:13px;right:13px;height:1.5px;background:rgba(255,255,255,.85)}
  .tier-text{position:absolute;left:10px;right:10px;top:196px;text-align:center;font-size:8.6px;font-weight:700;
    line-height:17px;color:var(--white)}

  .footer{position:absolute;left:0;top:862px;width:655px;height:103px;background:var(--amber);color:var(--white)}
  .f-col{position:absolute;top:10px;font-size:7.6px;line-height:12.7px}
  .f-col b{font-weight:700}
  .f-div{position:absolute;top:12px;width:1px;height:46px;background:var(--white)}
  .f-rule{position:absolute;left:5px;right:5px;top:69px;height:1px;background:var(--white)}
  .badge{position:absolute;top:77px;width:20px;height:20px;border-radius:50%;background:#f3f3f3;border:2px solid #c9c9c9}
  .badge.wide{width:36px;height:10px;top:82px;border-radius:1px}
</style>
</head>
<body>
<main class="sheet">
  <div class="edge-rule"></div>

  <div class="logo-disc"></div>
  <div class="brand-dot"></div>
  <div class="brand-name">TIVA</div>
  <div class="brand-sub">NATURBALSAME</div>
  <div class="brand-tag">LUMEN TIVA</div>

  <p class="sender"><b>Kestner Medical Vertrieb GmbH</b> · Lindenweg 14 · 80331 München</p>

  <h1 class="title">PREISLISTE:</h1>
  <div class="title-rule"></div>
  <div class="fold-mark"></div>
  <p class="intro">Lorem ipsum dolor sit amet, consectetuer adipiscing elit, sed diam nonummy nibh euismod tincidunt ut laoreet dolore magna aliquam erat volutpat. Ut wisi enim ad minim veniam, quis nostrud exerci tation ullamcorper suscipit lobortis</p>

  <section class="tier" style="left:76px">
    <div class="tier-body"></div>
    <div class="medal"><div class="medal-art" role="img" aria-label="Markenillustration im Goldrahmen"></div></div>
    <div class="tier-label">STARTER</div>
    <div class="tier-qty">5 Tuben</div>
    <div class="tier-rule" style="top:147px"></div>
    <div class="tier-price">20,99 €</div>
    <div class="tier-rule" style="top:190px"></div>
    <p class="tier-text">TIVA Naturbalsam ist ein natürliches Wohlfühlpro-gramm für Muskeln, Gelenke, Knochen, Nerven, Sehnen und Bänder sowie bei Prellungen und Verbrennungen. Betroffene können die entspannende</p>
  </section>

  <section class="tier" style="left:268px">
    <div class="tier-body"></div>
    <div class="medal"><div class="medal-art" role="img" aria-label="Markenillustration im Goldrahmen"></div></div>
    <div class="tier-label">PREMIUM</div>
    <div class="tier-qty">20 Tuben</div>
    <div class="tier-rule" style="top:147px"></div>
    <div class="tier-price">20,99 €</div>
    <div class="tier-rule" style="top:190px"></div>
    <p class="tier-text">TIVA Naturbalsam ist ein natürliches Wohlfühlpro-gramm für Muskeln, Gelenke, Knochen, Nerven, Sehnen und Bänder sowie bei Prellungen und Verbrennungen. Betroffene können die entspannende</p>
  </section>

  <section class="tier" style="left:459px">
    <div class="tier-body"></div>
    <div class="medal"><div class="medal-art" role="img" aria-label="Markenillustration im Goldrahmen"></div></div>
    <div class="tier-label">SPECIAL</div>
    <div class="tier-qty">50 Tuben</div>
    <div class="tier-rule" style="top:147px"></div>
    <div class="tier-price">20,99 €</div>
    <div class="tier-rule" style="top:190px"></div>
    <p class="tier-text">TIVA Naturbalsam ist ein natürliches Wohlfühlpro-gramm für Muskeln, Gelenke, Knochen, Nerven, Sehnen und Bänder sowie bei Prellungen und Verbrennungen. Betroffene können die entspannende</p>
  </section>

  <footer class="footer">
    <div class="f-col" style="left:36px"><b>Kestner Medical Vertrieb GmbH</b><br>Lindenweg 14<br>80331 München<br>Deutschland</div>
    <div class="f-div" style="left:167px"></div>
    <div class="f-col" style="left:175px"><b>Telefon:</b>&nbsp;&nbsp;0049 89 123 456 10<br><b>Telefax:</b>&nbsp;&nbsp;0049 89 123 456 11<br><b>E-Mail:</b>&nbsp;&nbsp;&nbsp;&nbsp;bestellung@tiva-naturbalsam.de<br><b>Internet:</b>&nbsp;www.tiva-naturbalsam.de</div>
    <div class="f-div" style="left:346px"></div>
    <div class="f-col" style="left:355px"><b>Gesellschafter:</b> Jonas Feldner<br>Gesellschaft mit beschränkter Haftung<br>Amtsgericht München | HRB 100200<br><b>St.-Nr.:</b> 100/200/30040</div>
    <div class="f-div" style="left:504px"></div>
    <div class="f-col" style="left:512px">Nordbank<br><b>IBAN</b> DE00 1234 5678 9012 3456 00<br><b>BIC</b>&nbsp;&nbsp;&nbsp;NORDDEMMXXX</div>
    <div class="f-rule"></div>
    <div class="badge" style="left:67px"></div>
    <div class="badge" style="left:150px"></div>
    <div class="badge" style="left:232px"></div>
    <div class="badge" style="left:316px"></div>
    <div class="badge" style="left:401px"></div>
    <div class="badge" style="left:484px"></div>
    <div class="badge wide" style="left:570px"></div>
  </footer>
</main>
</body>
</html>
```